Global Yoga Apparel Brand Needs a Beautiful Website

We need a website design for a new Yoga brand called Vessa. We develop beautiful, stylish, sexy, comfortable yoga leggings, tops, and yoga apparel for women looking to feel their best, look their best and perform their best on and off the yoga mat.
This will go up at http://vessa.example/ (which is a landing page right now).
We would like to see simple and clean design where the focus will be on powerful images and clean background space. We will be using Shopify to start building on and here are three sites that we would love to see options based off of the look, layout and feel while making something unique at the same time:
1. Tumo.ca
2. marikoven.com
3. www.q-plume.com
The final design should look clean, beautiful, inspiring, powerful and empowering.
Target Market(s)
mostly Females 21-35 range but will be appealing to women over 35 as well.

```html
<!DOCTYPE html>
<html lang="en">
<head>
<meta charset="utf-8">
<title>Vessa — Yoga Apparel</title>
<link rel="stylesheet" href="https://fonts.googleapis.com/css2?family=Raleway:wght@300;400;600;700&family=Lato:wght@400;700&display=swap">
<style>
:root{
  --ink:#1b1b1b;
  --black:#000;
  --topbar:#2b2b2b;
  --white:#fff;
  --paper:#f1f1f1;
  --band:#e6e6e6;
  --footer:#d6d6d6;
  --line:#cfcfcf;
  --muted:#666;
  --accent-orange:#f39c12;
  --accent-green:#7cb342;
  --ornament:#c9b79a;
}
*{box-sizing:border-box;margin:0;padding:0}
html,body{width:1200px;height:2769px;overflow:hidden}
body{position:relative;font-family:"Lato",Arial,sans-serif;color:var(--ink);background:var(--white)}
.abs{position:absolute}
svg{display:block}

/* top bar */
.topbar{left:0;top:0;width:1200px;height:33px;background:var(--topbar);color:#ddd;font-size:11px}
.topbar .welcome{left:162px;top:10px}
.topbar .account{right:162px;top:10px;display:flex;gap:22px}
.topbar .account span{display:flex;align-items:center;gap:5px}

/* header */
.header{left:0;top:33px;width:1200px;height:87px;background:var(--black)}
.logo{left:162px;top:14px;font-family:"Raleway",sans-serif;font-weight:700;font-size:46px;color:var(--white);letter-spacing:1px}
.nav{left:515px;top:39px;display:flex;gap:0;font-family:"Raleway",sans-serif;font-size:11px;font-weight:600;color:var(--white);letter-spacing:.5px}
.nav a{color:inherit;text-decoration:none;margin-right:40px}
.nav a.active{color:var(--white)}
.icon-btn{top:31px;width:26px;height:26px;border:2px solid var(--white);border-radius:50%}
.badge{position:absolute;top:-7px;right:-7px;width:13px;height:13px;border-radius:50%;font-size:8px;color:#fff;text-align:center;line-height:13px}

/* search */
.searchbar{left:0;top:120px;width:1200px;height:37px;background:var(--band);border-bottom:1px solid var(--line)}
.categories{left:162px;top:0;width:259px;height:37px;border-left:1px solid var(--line);border-right:1px solid var(--line);display:flex;align-items:center;padding:0 12px;font-size:13px;color:#555;gap:10px}
.categories .caret{margin-left:auto}
.search-field{left:421px;top:0;width:617px;height:37px;display:flex;align-items:center;padding-left:10px;font-size:11px;color:#999;border-right:1px solid var(--line)}
.search-field .glass{position:absolute;right:0;top:0;width:34px;height:37px;border-left:1px solid var(--line);display:flex;align-items:center;justify-content:center}

/* hero */
.hero{left:0;top:157px;width:1200px;height:437px;background:linear-gradient(100deg,#3d4a2c 0%,#5b6b3b 30%,#7d8a55 55%,#4a5a33 80%,#2f3a22 100%)}
.hero-title{right:162px;top:140px;font-family:"Raleway",sans-serif;font-weight:300;font-size:56px;color:var(--white);letter-spacing:2px}
.hero-sub{right:162px;top:216px;font-family:"Raleway",sans-serif;font-size:22px;color:var(--white)}
.hero-btn{right:162px;top:273px;width:152px;height:43px;border:2px solid var(--white);color:var(--white);font-family:"Raleway",sans-serif;font-weight:600;font-size:17px;display:flex;align-items:center;justify-content:center}
.slide-arrow{width:32px;height:32px;background:#222;border:1px solid #888;display:flex;align-items:center;justify-content:center}

/* section headings */
.sec-title{left:0;width:1200px;text-align:center;font-family:"Raleway",sans-serif;font-weight:400;font-size:25px;letter-spacing:1px;color:var(--ink)}
.sec-title b{font-weight:700}
.rule{left:570px;width:60px;height:1px;background:var(--ornament)}

.about{left:0;top:594px;width:1200px;height:305px;background:var(--paper)}
.about-text{left:162px;top:127px;width:876px;text-align:center;font-size:11.5px;line-height:19px;color:#444}
.outline-btn{border:1px solid #555;background:var(--white);font-size:11px;font-weight:700;display:flex;align-items:center;justify-content:center;color:var(--ink)}

/* products */
.products{left:0;width:1200px;height:535px}
.card-frame{border:1px solid var(--line);background:var(--white)}
.prod-img{width:203px;height:288px;background:linear-gradient(180deg,#f0f0f0,#e2e2e2)}
.prod-name{width:203px;text-align:center;font-size:10px;color:#444;letter-spacing:.3px}
.prod-price{width:203px;text-align:center;font-size:11px;font-weight:700}
.cart-btn{width:102px;height:24px;background:#1e1e1e;color:#fff;font-size:8px;display:flex;align-items:center;justify-content:center;gap:5px;letter-spacing:.5px}
.chev{width:20px;height:20px}

/* blog */
.blog-card{top:2106px;width:425px;height:211px;background:#ececec}
.blog-img{left:0;top:0;width:216px;height:211px}
.date{top:15px;left:171px;display:flex}
.date .day{width:46px;height:30px;background:#2a2a2a;color:#fff;font-family:"Raleway",sans-serif;font-weight:700;font-size:19px;display:flex;align-items:center;justify-content:center}
.date .mon{width:46px;height:30px;background:#7a7a7a;color:#fff;font-size:7px;line-height:9px;padding:6px 0 0 6px}
.blog-body{left:232px;top:20px;width:180px}
.blog-meta{text-align:right;font-size:9px;color:#333;display:flex;justify-content:flex-end;gap:5px;align-items:center}
.blog-head{margin-top:22px;font-size:9px;font-weight:700;color:#222}
.blog-text{margin-top:9px;font-size:9px;line-height:13px;color:#777}
.blog-more{margin-top:14px;width:90px;height:26px;font-size:10px}

/* features */
.features{left:0;top:2387px;width:1200px;height:78px;background:var(--band)}
.feature{top:26px;display:flex;align-items:center;gap:8px;font-size:9.5px;line-height:12px;color:#333}
.feature b{font-weight:700}

/* footer */
.footer{left:0;top:2465px;width:1200px;height:258px;background:var(--footer)}
.f-head{font-size:11px;color:#333;letter-spacing:.5px}
.contact-row{display:flex;align-items:center;gap:16px;font-size:10px;color:#444;line-height:13px}
.contact-row .circ{width:24px;height:24px;border:1px solid #444;border-radius:50%;display:flex;align-items:center;justify-content:center;flex:none}
.f-links{font-size:9.5px;color:#333;line-height:24px;list-style:none}
.f-links li::before{content:"› ";font-weight:700}
.f-logo{left:895px;top:82px;font-family:"Raleway",sans-serif;font-weight:700;font-size:70px;color:#555}
.social{top:186px;display:flex;gap:8px;left:914px}
.social span{width:24px;height:24px;display:block}
.sub-input{left:417px;top:166px;width:138px;height:27px;background:#555;color:#ddd;font-size:9px;display:flex;align-items:center;padding-left:10px;gap:6px}
.sub-btn{left:555px;top:166px;width:80px;height:27px;background:#1e1e1e;color:#fff;font-size:10px;font-weight:700;display:flex;align-items:center;justify-content:center}
.copyright{left:0;top:2723px;width:1200px;height:46px;background:#2a2a2a;color:#ccc;font-size:10px;text-align:center;line-height:46px}
</style>
</head>
<body>

<div class="abs topbar">
  <div class="abs welcome">Welcome To VESSA</div>
  <div class="abs account">
    <span><svg width="9" height="10" viewBox="0 0 9 10"><rect x="1" y="4" width="7" height="6" fill="#ddd"/><path d="M2.5 4V2.5a2 2 0 014 0V4" stroke="#ddd" fill="none"/></svg>Login or Register</span>
    <span><svg width="9" height="10" viewBox="0 0 9 10"><circle cx="4.5" cy="3" r="2.5" fill="#ddd"/><path d="M0 10a4.5 4 0 019 0z" fill="#ddd"/></svg>My Account</span>
  </div>
</div>

<header class="abs header">
  <div class="abs logo">vessa</div>
  <nav class="abs nav"><a class="active" href="#">HOME</a><a href="#">ABOUT US</a><a href="#">WOMEN</a><a href="#">BLOG</a><a href="#">CONTACT US</a></nav>
  <div class="abs icon-btn" style="left:964px">
    <svg width="22" height="22" viewBox="0 0 22 22"><path d="M11 16l-4.5-4.3a2.7 2.7 0 014.5-3 2.7 2.7 0 014.5 3z" fill="#fff"/></svg>
    <span class="badge" style="background:var(--accent-orange)">0</span>
  </div>
  <div class="abs icon-btn" style="left:1006px">
    <svg width="22" height="22" viewBox="0 0 22 22"><path d="M5 7h2l1.5 6h6l1.5-4.5H8" stroke="#fff" stroke-width="1.5" fill="none"/><circle cx="9" cy="15.5" r="1" fill="#fff"/><circle cx="14" cy="15.5" r="1" fill="#fff"/></svg>
    <span class="badge" style="background:var(--accent-green)">0</span>
  </div>
</header>

<div class="abs searchbar">
  <div class="abs categories">
    <svg width="14" height="11" viewBox="0 0 14 11"><path d="M0 1h14M0 5.5h14M0 10h14" stroke="#666" stroke-width="1.5"/></svg>
    All Categories
    <svg class="caret" width="8" height="5" viewBox="0 0 8 5"><path d="M0 0l4 5 4-5z" fill="#555"/></svg>
  </div>
  <div class="abs search-field">Search
    <span class="glass"><svg width="13" height="13" viewBox="0 0 13 13"><circle cx="5.5" cy="5.5" r="4.3" stroke="#555" stroke-width="1.6" fill="none"/><path d="M8.7 8.7L12 12" stroke="#555" stroke-width="1.8"/></svg></span>
  </div>
</div>

<section class="abs hero" role="img" aria-label="Woman in a blue tank top doing a seated yoga twist outdoors among green foliage">
  <div class="abs slide-arrow" style="left:2px;top:200px"><svg width="8" height="12" viewBox="0 0 8 12"><path d="M7 1L2 6l5 5" stroke="#fff" stroke-width="2" fill="none"/></svg></div>
  <div class="abs slide-arrow" style="right:2px;top:200px"><svg width="8" height="12" viewBox="0 0 8 12"><path d="M1 1l5 5-5 5" stroke="#fff" stroke-width="2" fill="none"/></svg></div>
  <h1 class="abs hero-title">YOGA APPAREL</h1>
  <p class="abs hero-sub">Right Place To Buy Yoga Leggings, Tops</p>
  <div class="abs hero-btn">SHOP NOW</div>
</section>

<section class="abs about">
  <h2 class="abs sec-title" style="top:55px">ABOUT <b>VESSA</b></h2>
  <div class="abs rule" style="top:97px"></div>
  <p class="abs about-text">Lorem ipsum dolor sit amet, consectetuer adipiscing elit, sed diam nonummy nibh euismod tincidunt ut laoreet dolore magna aliquam erat volutpat. Ut wisi enim ad minim veniam, quis nostrud exerci tation ullamcorper suscipit lobortis nisl ut aliquip ex ea commodo consequat. Duis autem vel eum iriure dolor in hendrerit in vulputate velit esse molestie consequat, vel illum dolore eu feugiat nulla facilisis at vero</p>
  <div class="abs outline-btn" style="left:541px;top:209px;width:118px;height:33px">Read More »</div>
</section>

<!-- New products -->
<section class="abs products" style="top:899px;background:var(--white)">
  <h2 class="abs sec-title" style="top:52px">NEW <b>PRODUCTS</b></h2>
  <div class="abs rule" style="top:100px"></div>
  <svg class="abs chev" style="left:115px;top:267px" viewBox="0 0 20 20"><path d="M13 3l-7 7 7 7" stroke="#222" stroke-width="3" fill="none"/></svg>
  <svg class="abs chev" style="left:1065px;top:267px" viewBox="0 0 20 20"><path d="M7 3l7 7-7 7" stroke="#222" stroke-width="3" fill="none"/></svg>
  <div class="abs card-frame" style="left:157px;top:133px;width:212px;height:393px"></div>
  <div class="abs prod-img" style="left:162px;top:138px" role="img" aria-label="Black leggings with grey knee panels on a model"></div>
  <div class="abs prod-img" style="left:386px;top:138px" role="img" aria-label="Black cropped leggings with side cut-outs on a model"></div>
  <div class="abs prod-img" style="left:611px;top:138px" role="img" aria-label="Grey strappy-back yoga tank on a model"></div>
  <div class="abs prod-img" style="left:836px;top:138px" role="img" aria-label="Black strappy sports top seen from the back"></div>
  <div class="abs prod-name" style="left:162px;top:442px">FLOW BOTTOMS LEGGINGS</div>
  <div class="abs prod-name" style="left:386px;top:442px">GLOW 3/4 LEGGINGS</div>
  <div class="abs prod-name" style="left:611px;top:440px">WOMEN'S BLISS TANK</div>
  <div class="abs prod-name" style="left:836px;top:440px">WOMEN'S GRADIENT TANK</div>
  <div class="abs prod-price" style="left:162px;top:464px">$50.00</div>
  <div class="abs prod-price" style="left:386px;top:464px">$50.00</div>
  <div class="abs prod-price" style="left:611px;top:462px">$50.00</div>
  <div class="abs prod-price" style="left:836px;top:462px">$50.00</div>
  <div class="abs cart-btn" style="left:212px;top:486px"><svg width="9" height="8" viewBox="0 0 9 8"><path d="M0 0h2l1 5h5l1-4H2.5" stroke="#fff" fill="none"/><circle cx="3.5" cy="7" r=".8" fill="#fff"/><circle cx="7" cy="7" r=".8" fill="#fff"/></svg>ADD TO CART</div>
</section>

<!-- Special products -->
<section class="abs products" style="top:1434px;height:532px;background:var(--band)">
  <h2 class="abs sec-title" style="top:56px">SPECIAL <b>PRODUCTS</b></h2>
  <div class="abs rule" style="top:102px"></div>
  <svg class="abs chev" style="left:115px;top:282px" viewBox="0 0 20 20"><path d="M13 3l-7 7 7 7" stroke="#fff" stroke-width="3" fill="none"/></svg>
  <svg class="abs chev" style="left:1065px;top:282px" viewBox="0 0 20 20"><path d="M7 3l7 7-7 7" stroke="#fff" stroke-width="3" fill="none"/></svg>
  <div class="abs card-frame" style="left:157px;top:135px;width:212px;height:393px"></div>
  <div class="abs prod-img" style="left:162px;top:141px;background:linear-gradient(180deg,#fafafa,#eeeeee)" role="img" aria-label="Dark leggings with sheer mesh panels on a model"></div>
  <div class="abs prod-img" style="left:386px;top:141px;background:linear-gradient(180deg,#fafafa,#eeeeee)" role="img" aria-label="Black leggings with mesh inserts on a model"></div>
  <div class="abs prod-img" style="left:611px;top:141px;background:linear-gradient(180deg,#fafafa,#e3f2ef)" role="img" aria-label="Mint perforated tank top seen from the back"></div>
  <div class="abs prod-img" style="left:836px;top:141px;background:linear-gradient(180deg,#fafafa,#eeeeee)" role="img" aria-label="White cross-back tank over black sports bra"></div>
  <div class="abs prod-name" style="left:162px;top:449px">FLOW BOTTOMS LEGGINGS</div>
  <div class="abs prod-name" style="left:386px;top:449px">GLOW 3/4 LEGGINGS</div>
  <div class="abs prod-name" style="left:611px;top:449px">WOMEN'S BLISS TANK</div>
  <div class="abs prod-name" style="left:836px;top:449px">WOMEN'S GRADIENT TANK</div>
  <div class="abs prod-price" style="left:162px;top:471px">$50.00</div>
  <div class="abs prod-price" style="left:386px;top:471px">$50.00</div>
  <div class="abs prod-price" style="left:611px;top:471px">$50.00</div>
  <div class="abs prod-price" style="left:836px;top:471px">$50.00</div>
  <div class="abs cart-btn" style="left:212px;top:493px"><svg width="9" height="8" viewBox="0 0 9 8"><path d="M0 0h2l1 5h5l1-4H2.5" stroke="#fff" fill="none"/><circle cx="3.5" cy="7" r=".8" fill="#fff"/><circle cx="7" cy="7" r=".8" fill="#fff"/></svg>ADD TO CART</div>
</section>

<!-- Blog -->
<h2 class="abs sec-title" style="top:2020px">LATEST <b>BLOG</b></h2>
<div class="abs rule" style="top:2066px"></div>

<article class="abs blog-card" style="left:162px">
  <div class="abs blog-img" role="img" aria-label="Yoga class with many students stretching on mats in a bright studio" style="background:linear-gradient(160deg,#d9cfc2,#a89684 55%,#6d5f55)"></div>
  <div class="abs date"><div class="day">17</div><div class="mon">OCT<br>2016</div></div>
  <div class="abs blog-body">
    <div class="blog-meta"><svg width="11" height="9" viewBox="0 0 11 9"><path d="M1 1h7v5H4l-2 2V6H1z" stroke="#333" fill="none"/></svg>1,256</div>
    <div class="blog-head">LOREM : IPSUM IS SIMPLY DUMMY</div>
    <div class="blog-text">Contrary to popular belief, Lorem Ipsum is not simply random text.</div>
    <div class="outline-btn blog-more">Read More »</div>
  </div>
</article>

<article class="abs blog-card" style="left:613px">
  <div class="abs blog-img" role="img" aria-label="Women practising seated yoga on purple mats in a studio" style="background:linear-gradient(160deg,#e6e0d8,#b7aca0 50%,#7a6a82)"></div>
  <div class="abs date"><div class="day">17</div><div class="mon">OCT<br>2016</div></div>
  <div class="abs blog-body">
    <div class="blog-meta"><svg width="11" height="9" viewBox="0 0 11 9"><path d="M1 1h7v5H4l-2 2V6H1z" stroke="#333" fill="none"/></svg>1,256</div>
    <div class="blog-head">LOREM : IPSUM IS SIMPLY DUMMY</div>
    <div class="blog-text">Contrary to popular belief, Lorem Ipsum is not simply random text.</div>
    <div class="outline-btn blog-more">Read More »</div>
  </div>
</article>

<!-- Features -->
<section class="abs features">
  <div class="abs feature" style="left:236px">
    <svg width="22" height="16" viewBox="0 0 22 16"><rect x="0" y="2" width="13" height="9" fill="#222"/><path d="M13 5h5l3 3v3h-8z" fill="#222"/><circle cx="4" cy="13" r="2" fill="#222"/><circle cx="17" cy="13" r="2" fill="#222"/></svg>
    <div><b>FREE SHIPPING</b><br>on order over $100.00</div>
  </div>
  <div class="abs feature" style="left:515px">
    <svg width="20" height="20" viewBox="0 0 20 20"><path d="M16 10a6 6 0 11-2-4.5" stroke="#222" stroke-width="2.5" fill="none"/><path d="M12 2h5v5z" fill="#222"/></svg>
    <div><b>FREE RETURNS</b><br>free 90 days return policy</div>
  </div>
  <div class="abs feature" style="left:808px">
    <svg width="20" height="18" viewBox="0 0 20 18"><rect x="1" y="5" width="18" height="4" fill="#222"/><rect x="2.5" y="9" width="15" height="8" fill="#222"/><rect x="9" y="5" width="2" height="12" fill="#e6e6e6"/><path d="M10 5C7 0 3 2 6 5M10 5c3-5 7-3 4 0" stroke="#222" stroke-width="1.6" fill="none"/></svg>
    <div><b>FREE GIFT</b><br>register and get free gift</div>
  </div>
</section>

<!-- Footer -->
<footer class="abs footer">
  <div class="abs f-head" style="left:162px;top:60px">CONTACT US</div>
  <div class="abs contact-row" style="left:162px;top:100px"><span class="circ"><svg width="10" height="12" viewBox="0 0 10 12"><path d="M5 12S1 7 1 4.5a4 4 0 018 0C9 7 5 12 5 12z" fill="#444"/><circle cx="5" cy="4.5" r="1.5" fill="#d6d6d6"/></svg></span>Lorem ipsum dolor sit amet,<br>consectetuer adipiscing elit</div>
  <div class="abs contact-row" style="left:162px;top:144px;font-size:15px"><span class="circ"><svg width="11" height="11" viewBox="0 0 11 11"><path d="M2 0l2 3-1 1.5a7 7 0 003.5 3.5L8 7l3 2-1.5 2C5 11 0 6 0 1.5z" fill="#444"/></svg></span>123-456-7890</div>
  <div class="abs contact-row" style="left:162px;top:186px"><span class="circ"><svg width="11" height="8" viewBox="0 0 11 8"><rect width="11" height="8" fill="#444"/><path d="M0 0l5.5 4L11 0" stroke="#d6d6d6" fill="none"/></svg></span>support@vessa.example</div>

  <div class="abs f-head" style="left:417px;top:60px">NEWSLETTER SIGNUP</div>
  <p class="abs" style="left:417px;top:100px;width:110px;font-size:9.5px;line-height:13px;color:#444">Get the latest updates by entering your email address</p>
  <svg class="abs" style="left:540px;top:100px" width="70" height="52" viewBox="0 0 70 52"><path d="M2 8L68 2 40 50 30 30z" fill="none" stroke="#aaa" stroke-width="1.5"/><path d="M30 30L68 2" stroke="#aaa" stroke-width="1.5"/></svg>
  <div class="abs sub-input"><svg width="10" height="7" viewBox="0 0 10 7"><rect width="10" height="7" fill="#bbb"/><path d="M0 0l5 3.5L10 0" stroke="#555" fill="none"/></svg>Enter your email here</div>
  <div class="abs sub-btn">SUBSCRIBE</div>

  <div class="abs f-head" style="left:716px;top:60px">ABOUT US</div>
  <ul class="abs f-links" style="left:716px;top:88px">
    <li>Home</li><li>About Us</li><li>Women</li><li>Blog</li><li>Contact Us</li>
  </ul>

  <div class="abs f-logo">vessa</div>
  <div class="abs social" aria-label="Social links">
    <span style="background:#3b5998"></span>
    <span style="background:#1da1f2"></span>
    <span style="background:#dd4b39"></span>
    <span style="background:#c0392b"></span>
  </div>
</footer>

<div class="abs copyright">Copyright © 2016 VESSA. All Rights Reserved.</div>

</body>
</html>
```